Elegant One-Page Flyer That Catches People's Eye

For a series of workshops and zoom calls I am marketing with a colleague of mine, we would like to have an elegant, catchy one-page flyer that entices people to contact us. I am envisioning a one-page flyer (a card that is somewhat larger than a postcard) with great text, layout and images which magnetically draws people to us and is positive and inspiring. Also, if at all possible, a QR code linking it to our websites. Good colours would be shades of blue and green. I am uploading: the Text, our pictures, logos and contact information.

```html
<!DOCTYPE html>
<html lang="en">
<head>
<meta charset="utf-8">
<title>Rising above Hidden Career Deal breakers – Workshop Flyer</title>
<link href="https://fonts.googleapis.com/css2?family=Montserrat:wght@400;500;600;700&display=swap" rel="stylesheet">
<style>
  :root{
    --green:#8fbf5e;
    --green-dark:#6b8e3a;
    --maroon:#5c1a1f;
    --ink:#262626;
    --pill-dark:#2b2b2b;
    --paper:#ffffff;
    --paper-grey:#eeeeee;
    --stage:#d9d9d9;
    --sky-top:#3d6fb3;
    --sky-mid:#9dbde0;
    --mountain:#4f5d70;
  }
  *{box-sizing:border-box;margin:0;padding:0}
  html,body{width:1200px;height:1014px;overflow:hidden}
  body{background:var(--stage);font-family:"Montserrat",sans-serif;color:var(--ink);position:relative}

  .flyer{
    position:absolute;left:24px;top:100px;
    width:1280px;height:904px;
    transform:scale(0.9);transform-origin:0 0;
    background:linear-gradient(180deg,var(--paper-grey) 0%,var(--paper) 60%);
    overflow:hidden;
  }
  .shapes{position:absolute;inset:0}

  .brand{position:absolute;display:flex;align-items:center;gap:12px}
  .brand--primary{left:52px;top:62px;font-size:40px;font-weight:500;color:var(--green-dark)}
  .brand--primary .brand-dot{width:46px;height:46px;border-radius:50%;border:2px solid var(--green-dark)}
  .brand-divider{position:absolute;left:407px;top:50px;width:1px;height:75px;background:#b5b5b5}
  .brand--partner{left:438px;top:62px;flex-direction:column;align-items:flex-end;font-size:32px;font-weight:500;color:var(--maroon);line-height:1.05;gap:0}
  .brand--partner small{font-size:17px}

  .questions{position:absolute;left:51px;top:160px;font-size:18.5px;font-weight:600;line-height:26px}
  .headline{position:absolute;left:51px;top:250px;font-size:35px;font-weight:700;line-height:51px}
  .headline .accent{color:var(--green)}
  .headline .strong{color:var(--maroon)}

  .format-label{position:absolute;left:56px;top:356px;font-size:26px;font-weight:600}
  .format-box{position:absolute;left:57px;top:373px;width:450px;height:103px;border:1px dotted #777;border-radius:6px;padding:24px 20px 0 21px;font-size:19px;font-weight:500;line-height:31px}

  .contact-lead{position:absolute;left:60px;top:517px;font-size:20px;font-weight:600;line-height:29px}
  .section-pill{position:absolute;left:50px;top:588px;height:31px;padding:0 18px;border-radius:16px;background:var(--pill-dark);color:#fff;font-size:17px;font-weight:700;line-height:31px}
  .section-rule{position:absolute;left:202px;top:603px;width:373px;height:1px;background:#4a4a4a}

  .facilitator{position:absolute;left:52px;width:540px}
  .facilitator .portrait{position:absolute;left:0;top:0;width:112px;height:112px;border-radius:50%;border:5px solid #fff}
  .facilitator .info{position:absolute;left:138px;top:0;width:400px}
  .facilitator h3{font-size:16px;font-weight:700;color:var(--maroon)}
  .facilitator p{font-size:12px;font-weight:500;line-height:17px;margin-top:6px}
  .contact-row{display:flex;margin-top:10px}
  .contact-row .email{display:flex;align-items:center;gap:8px;height:27px;padding:0 18px 0 6px;border-radius:14px;background:var(--maroon);color:#fff;font-size:14px;font-weight:500;position:relative;z-index:1}
  .contact-row .phone{display:flex;align-items:center;gap:6px;height:27px;padding:0 12px 0 22px;margin-left:-14px;border-radius:0 14px 14px 0;background:#fff;font-size:14px;font-weight:600}
  .icon{width:16px;height:16px;flex:none}

  .facilitator--one{top:642px}
  .facilitator--one .portrait{background:#7d6a55;top:0}
  .facilitator--one .info{top:-10px}
  .facilitator--two{top:773px}
  .facilitator--two .portrait{background:#c9b7a6}
  .facilitator--two .info{top:6px;left:135px}

  .benefits{position:absolute;left:731px;top:686px;width:500px}
  .benefits h2{font-size:21.5px;font-weight:700;line-height:32px}
  .benefits ul{list-style:none;margin-top:14px}
  .benefits li{display:flex;align-items:center;gap:14px;font-size:15.5px;font-weight:500;height:29px}
  .tick{width:18px;height:18px;flex:none}
</style>
</head>
<body>
<main class="flyer">
  <svg class="shapes" width="1280" height="904" viewBox="0 0 1280 904">
    <defs>
      <linearGradient id="sky" x1="0" y1="0" x2="0.3" y2="1">
        <stop offset="0" stop-color="var(--sky-top)"/>
        <stop offset="0.55" stop-color="var(--sky-mid)"/>
        <stop offset="1" stop-color="var(--mountain)"/>
      </linearGradient>
    </defs>
    <path class="band-green" fill="var(--green)" d="M0 495 H568 Q582 495 592 508 L690 640 Q700 655 716 655 H1280 V904 H0 Z"/>
    <line class="accent-capsule" x1="800" y1="112" x2="950" y2="-20" stroke="var(--green)" stroke-width="72" stroke-linecap="round"/>
    <line class="accent-capsule" x1="1215" y1="505" x2="1300" y2="420" stroke="var(--maroon)" stroke-width="62" stroke-linecap="round"/>
    <path class="hero-photo" role="img" aria-label="Photo: a climber in a red jacket hanging from a rope against a bright cloudy sky above mountain peaks" fill="url(#sky)" d="M978 0 H1280 V385 L1065 600 C965 690 775 665 705 505 C668 420 690 335 742 272 Z"/>
  </svg>

  <div class="brand brand--primary"><span class="brand-dot"></span>BrightPath</div>
  <div class="brand-divider"></div>
  <div class="brand brand--partner">Harwell Coaching<small>Zürich</small></div>

  <p class="questions">Is your career going the way you want?<br>If not, do you feel stuck? Blocked? Frustrated?<br>Don’t know what to do about this?</p>

  <h1 class="headline"><span class="accent">Rising above Hidden</span><br><span class="strong">Career Deal breakers</span></h1>

  <div class="format-label">Format:</div>
  <div class="format-box">4 Mini-Workshops + 2 short Online Group Coaching Sessions between Workshops</div>

  <p class="contact-lead">For dates, venue and further information<br>contact Clara or Nora at</p>

  <div class="section-pill">Facilitators:</div>
  <div class="section-rule"></div>

  <section class="facilitator facilitator--one">
    <div class="portrait" role="img" aria-label="Portrait photo of Dr. Nora Whitfield"></div>
    <div class="info">
      <h3>Dr. Nora Whitfield</h3>
      <p>PhD, CPC, is an American &amp; Swiss-Trained Work &amp; Organizational Psychologist, ICF-Certified Coach, Board Certified Hypnotherapist, Certified Naturopath (TEN) &amp; Certified Ayurvedic Practitioner.</p>
      <div class="contact-row">
        <span class="email"><svg class="icon" viewBox="0 0 16 16"><circle cx="8" cy="8" r="8" fill="#fff"/><rect x="4" y="5" width="8" height="6" rx="1" fill="var(--maroon)"/><path d="M4 5.5 8 8.5 12 5.5" stroke="#fff" fill="none" stroke-width="1"/></svg>nora@brightpath-example.ch</span>
        <span class="phone"><svg class="icon" viewBox="0 0 16 16"><circle cx="8" cy="8" r="8" fill="var(--green-dark)"/><path d="M5.5 4.5c.5-.3 1-.2 1.2.3l.5 1.2c.1.4 0 .7-.3.9l-.4.3c.5 1 1.2 1.7 2.2 2.2l.3-.4c.2-.3.6-.4.9-.3l1.2.5c.5.2.6.7.3 1.2-.6.9-1.5 1.1-2.5.6C7 10.2 5.8 9 5 7.2c-.4-1 -.3-2 .5-2.7z" fill="#fff"/></svg>076 555 0142</span>
      </div>
    </div>
  </section>

  <section class="facilitator facilitator--two">
    <div class="portrait" role="img" aria-label="Portrait photo of Dr. Clara Brunner"></div>
    <div class="info">
      <h3>Dr. Clara Brunner</h3>
      <p>Ph.D., PCC is a coach and somatic experience practitioner ,<br>a team coach with diploma and a certified virtual team coach.</p>
      <div class="contact-row">
        <span class="email"><svg class="icon" viewBox="0 0 16 16"><circle cx="8" cy="8" r="8" fill="#fff"/><rect x="4" y="5" width="8" height="6" rx="1" fill="var(--maroon)"/><path d="M4 5.5 8 8.5 12 5.5" stroke="#fff" fill="none" stroke-width="1"/></svg>clara@harwell-example.ch</span>
        <span class="phone"><svg class="icon" viewBox="0 0 16 16"><circle cx="8" cy="8" r="8" fill="var(--green-dark)"/><path d="M5.5 4.5c.5-.3 1-.2 1.2.3l.5 1.2c.1.4 0 .7-.3.9l-.4.3c.5 1 1.2 1.7 2.2 2.2l.3-.4c.2-.3.6-.4.9-.3l1.2.5c.5.2.6.7.3 1.2-.6.9-1.5 1.1-2.5.6C7 10.2 5.8 9 5 7.2c-.4-1 -.3-2 .5-2.7z" fill="#fff"/></svg>079 555 01 87</span>
      </div>
    </div>
  </section>

  <section class="benefits">
    <h2>Learn to overcome and rise above the<br>4 top hidden career deal breakers fast:</h2>
    <ul>
      <li><svg class="tick" viewBox="0 0 18 18"><circle cx="9" cy="9" r="9" fill="var(--maroon)"/><path d="M5 9.2 7.8 12 13 6.5" stroke="#fff" stroke-width="2" fill="none"/></svg>Microaggressions</li>
      <li><svg class="tick" viewBox="0 0 18 18"><circle cx="9" cy="9" r="9" fill="var(--maroon)"/><path d="M5 9.2 7.8 12 13 6.5" stroke="#fff" stroke-width="2" fill="none"/></svg>Toxic black box team dynamics</li>
      <li><svg class="tick" viewBox="0 0 18 18"><circle cx="9" cy="9" r="9" fill="var(--maroon)"/><path d="M5 9.2 7.8 12 13 6.5" stroke="#fff" stroke-width="2" fill="none"/></svg>Workplace snakes and other dysfunctional types</li>
      <li><svg class="tick" viewBox="0 0 18 18"><circle cx="9" cy="9" r="9" fill="var(--maroon)"/><path d="M5 9.2 7.8 12 13 6.5" stroke="#fff" stroke-width="2" fill="none"/></svg>Disempowering Subconscious Algorithmsno</li>
    </ul>
  </section>
</main>
</body>
</html>
```